Harbourline Strategy Group firm

I need a business card that is succint for a Brisbane based business called Harbourline Strategy Group Pty Ltd.
We bridge the gaps between People, Process and Technology.

We are a specialist operational excellence firm, delivering strategic consulting and business advisory services in six core capabilities, across all industries and all business lines to improve performance, efficiency, profitability, automation and scalability, for clients across Australia &New Zealand.
Updates

Hi Designers, I have uploaded the logo in 3D .png format, to assist in card design.

Target Market(s)

Project Management professionals, IT professionals, corporate and government clients managing transitioning or transformation projects.

Contact Information for Business Card

Harbourline Strategy Group Pty Ltd

Daniel Ferreira
Principal Consultant

mobile: +61 417 260 315
email: daniel@harbourlinestrategygroup.com.au
webpage: www.harbourlinestrategygroup.com

professional services: strategic advisors,

Font styles to use
Sans Serif

Requirements
Must have
• Business name: Harbourline Strategy Group
logo: attached
Contact person: Daniel Ferreira
Title: Principal Consultant
contact details:
mobile +61 417 260
email: daniel@HarbourlineStrategyGroup.com.au
website: HarbourlineStrategyGroup.com

on back side with logo include: A.B.N. 58210947362

professional services offered: Business Analysis, Strategic Advisory
Nice to have
• QR code
Should not have
• contacts picture

```html
<!DOCTYPE html>
<html lang="en">
<head>
<meta charset="utf-8">
<title>Harbourline Strategy Group – Business Card</title>
<link rel="stylesheet" href="https://fonts.googleapis.com/css2?family=Mulish:wght@400;600;700;800&display=swap">
<style>
  :root {
    --backdrop: #1d1d1d;
    --paper: #ececec;
    --paper-light: #f2f2f2;
    --navy: #1f2645;
    --red: #d21f26;
    --ink: #3a3a3a;
    --muted: #6a6a6a;
    --rule: #9a9a9a;
  }
  * { margin: 0; padding: 0; box-sizing: border-box; }
  html, body { width: 1200px; height: 1138px; overflow: hidden; background: var(--backdrop); }
  body { position: relative; font-family: "Mulish", sans-serif; }

  .card {
    position: absolute;
    width: 622px;
    height: 376px;
    background: linear-gradient(180deg, var(--paper-light), var(--paper));
    overflow: hidden;
  }
  .card--front { left: 273px; top: 185px; }
  .card--back  { left: 275px; top: 607px; }

  /* wordmark */
  .wordmark {
    position: absolute;
    display: flex;
    align-items: center;
    color: var(--navy);
    font-family: "Mulish", sans-serif;
    font-weight: 800;
    text-transform: uppercase;
    line-height: 0.98;
  }
  .wordmark__square { background: var(--navy); flex: none; }
  .card--front .wordmark { left: 0; right: 0; top: 118px; justify-content: center; gap: 16px; font-size: 38px; }
  .card--front .wordmark__square { width: 46px; height: 46px; }
  .card--back .wordmark { left: 24px; top: 150px; gap: 10px; font-size: 24px; }
  .card--back .wordmark__square { width: 28px; height: 28px; }

  .abn {
    position: absolute;
    left: 62px; top: 210px;
    font-size: 12px; font-weight: 600;
    color: var(--muted);
    letter-spacing: 0.4px;
  }

  /* front website line */
  .front-web {
    position: absolute;
    left: 0; right: 0; top: 316px;
    display: flex; align-items: center; justify-content: center; gap: 20px;
    font-size: 14px; color: var(--ink); letter-spacing: 0.3px;
  }
  .front-web__rule { width: 42px; height: 2px; background: linear-gradient(90deg, transparent, var(--rule), transparent); }
  .front-web__accent { color: var(--red); }

  .band { position: absolute; left: 0; right: 0; bottom: 0; height: 11px; display: flex; }
  .band__red { width: 312px; background: var(--red); }
  .band__navy { flex: 1; background: var(--navy); }

  /* back details */
  .person { position: absolute; left: 304px; top: 104px; }
  .person__name { font-weight: 700; font-size: 24px; color: var(--red); line-height: 1.1; }
  .person__title { font-size: 15.5px; color: var(--ink); margin-top: 4px; }
  .person__services { font-size: 12px; font-weight: 600; color: var(--muted); margin-top: 4px; letter-spacing: 0.2px; }

  .contacts { position: absolute; left: 306px; top: 200px; list-style: none; }
  .contacts li { display: flex; align-items: center; height: 24px; font-size: 14px; color: var(--ink); letter-spacing: -0.2px; }
  .contacts svg { width: 13px; height: 13px; margin-right: 12px; flex: none; }
</style>
</head>
<body>

<section class="card card--front" aria-label="Front of card">
  <div class="wordmark">
    <span class="wordmark__square"></span>
    <span>Harbourline<br>Strategy Group</span>
  </div>
  <div class="front-web">
    <span class="front-web__rule"></span>
    <span>www.<span class="front-web__accent">harbourline</span>strategygroup.com</span>
    <span class="front-web__rule"></span>
  </div>
  <div class="band"><span class="band__red"></span><span class="band__navy"></span></div>
</section>

<section class="card card--back" aria-label="Back of card">
  <div class="wordmark">
    <span class="wordmark__square"></span>
    <span>Harbourline<br>Strategy Group</span>
  </div>
  <p class="abn">A.B.N. 58210947362</p>

  <div class="person">
    <p class="person__name">Daniel Ferreira</p>
    <p class="person__title">Principal Consultant</p>
    <p class="person__services">Business Analysis &nbsp;|&nbsp; Strategic Advisory</p>
  </div>

  <ul class="contacts">
    <li>
      <svg viewBox="0 0 16 16" aria-hidden="true"><path fill="#d21f26" d="M2 6c0-2 2-3 6-3s6 1 6 3l-3 1-1-2H6L5 7 2 6zm2 2h8l1 6H3l1-6zm4 1.5a2 2 0 100 4 2 2 0 000-4z"/></svg>
      +61 417 260 315
    </li>
    <li>
      <svg viewBox="0 0 16 16" aria-hidden="true"><rect x="1" y="3" width="14" height="10" fill="#d21f26"/><path d="M1.5 3.5 8 9l6.5-5.5" fill="none" stroke="#f2f2f2" stroke-width="1.3"/></svg>
      daniel@harbourlinestrategygroup.com.au
    </li>
    <li>
      <svg viewBox="0 0 16 16" aria-hidden="true"><g fill="none" stroke="#d21f26" stroke-width="1.3"><circle cx="8" cy="8" r="6.5"/><ellipse cx="8" cy="8" rx="3" ry="6.5"/><path d="M1.5 8h13M2.5 4.7h11M2.5 11.3h11"/></g></svg>
      www.harbourlinestrategygroup.com
    </li>
  </ul>
</section>

</body>
</html>
```